VelaNest needs a logo, webdesign, stationery and business card design!

VelaNest is a new company that specializes in helping and supporting elderly people. This can be helping in activities, like going out for a cup of coffee or a walk in the park, help in household like laundry and cleaning, accompanying to go to the hospital, or just have a nice conversation etc. Be aware that in the future activities may be expanded to help and support children as well, but our primary focus for now is elderly people.

Logo

VelaNest needs a logo design. Our initial thought is something like older hands holding a younger hand in order to express helping elderly people, but as said we might expand to help and support children in the future as well. The logo should express professionalism, reliability, that we help and support, and may have a 'medical'-look in some way. The text VelaNest must be included.

Website

In addition we need a web design as well, which should include the following pages:
- Homepage
- about us
- our services
- blog/news overview
- blog/news item
- contactpage with contactform
- social media icons to link to facebook and twitter
- we want a 'Like'-button for our facebook page on a place where people would most probably click on it

Most elderly people tend to work on a desktop/laptop computer or tablet. As such we want the website to be optimized for deskop and tablets. Smartphone is also important but less than desktop and tablet. As our primary focus is elderly people we need a good readable font. We also want options to increase/decrease font size included somewhere in the design. We would like to have some way of representing our services on the homepage. In addition, we would like to have a good call-to-action element with our phone number.

Stationery and business card

We want a matching stationery to be designed. Also, a double sided business card is required.
Updates

Thank you all for submitting the designs. We will review designs and get back to you later this week about what design we choose.

Target Market(s)

elderly people, disabled people, children that need extra support, disabled children

Industry/Entity Type

Health Care

Contact Information for Business Card

Will provide these details ASAP! You can use placeholder/dummy texts in the meanwhile

Logo Text

VelaNest

Number of Pages Required

5+ page

Font styles to use
Sans Serif

Requirements
Must have
• We chose the option to have you, the designer, choose colors, but the website doesn't save it. So, we want you to choose colors.
Should not have
• no things like wheelchairs as that is too much tailored on disabled people. We also support and help disabled people but it is not our primary focus.

```html
<!DOCTYPE html>
<html lang="en">
<head>
<meta charset="utf-8">
<title>VelaNest – Home</title>
<link href="https://fonts.googleapis.com/css2?family=Roboto:ital,wght@0,400;0,500;0,700;1,500&family=Lato:ital,wght@0,400;0,700;1,400&family=Raleway:wght@600;700&display=swap" rel="stylesheet">
<style>
:root{
  --teal:#5ab4c5;
  --ink:#4d4d4d;
  --text:#222;
  --light:#f2f2f2;
  --white:#fff;
  --footer-dark:#5e5e5e;
  --icon-dark:#4b4b4b;
}
*{margin:0;padding:0;box-sizing:border-box}
html,body{width:670px;height:1200px;overflow:hidden;background:var(--white)}
body{position:relative;font-family:'Lato',sans-serif;color:var(--text)}
a{text-decoration:none}
.abs{position:absolute}

/* top bar */
.topbar{top:0;left:0;width:670px;height:24px;border-bottom:1px solid #e6e6e6;font-size:8px;color:var(--ink)}
.topbar .contact{top:6px;display:flex;align-items:center;gap:5px}
.size-tools{top:5px;left:584px;display:flex;gap:3px}
.size-tools span{width:13px;height:13px;display:flex;align-items:center;justify-content:center;font:700 8px 'Roboto',sans-serif}
.size-tools .btn{background:var(--teal)}
.size-tools .plain{border:1px solid #333;color:#111;background:#fff}

/* header */
.brand{top:35px;left:45px;display:flex;align-items:center;gap:8px}
.brand .mark{width:34px;height:34px;border-radius:50%;background:var(--teal)}
.brand .name{font:400 21px 'Roboto',sans-serif;color:var(--teal)}
.nav a{position:absolute;top:47px;font:500 8.5px 'Roboto',sans-serif;color:#333;letter-spacing:.2px}
.nav a.active{top:42px;left:235px;width:45px;height:20px;background:var(--teal);color:#fff;display:flex;align-items:center;justify-content:center;border-radius:2px}

/* hero */
.hero{top:81px;left:0;width:670px;height:308px;background:
  radial-gradient(ellipse 150px 170px at 200px 160px,#d9a88e 0%,rgba(217,168,142,0) 100%),
  radial-gradient(ellipse 140px 160px at 310px 200px,#e8d7cc 0%,rgba(232,215,204,0) 100%),
  linear-gradient(90deg,#c9b8a2 0%,#e7e1d6 45%,#9bb6c9 75%,#6f93b5 100%)}
.hero .caption{left:0;bottom:0;width:670px;height:36px;background:rgba(40,40,40,.7);color:#fff;font:italic 500 17px 'Roboto',sans-serif;display:flex;align-items:center;justify-content:center}
.arrow{width:21px;height:21px;background:#2f2f2f;border:1px solid #999;display:flex;align-items:center;justify-content:center}

/* section titles */
.title{left:0;width:670px;text-align:center;font:500 18px 'Roboto',sans-serif;color:var(--ink)}
.title b{font-weight:500;color:var(--teal)}
.divider{left:285px;width:100px;height:12px}

/* welcome */
.welcome{top:389px;left:0;width:670px;height:204px;background:var(--light)}
.welcome p{top:82px;left:45px;width:580px;text-align:center;font-size:8.6px;line-height:14.3px;color:#222}
.cta{top:149px;left:291px;width:88px;height:22px;border-radius:11px;background:var(--teal);color:#fff;font:500 8px 'Roboto',sans-serif;display:flex;align-items:center;padding-left:15px}
.cta i{position:absolute;right:4px;top:4px;width:14px;height:14px;border-radius:50%;background:#fff}

/* services */
.service{top:684px;width:130px;text-align:center}
.service .icon{margin:0 auto;width:64px;height:64px;border-radius:50%;background:#f3f3f3;border:1px solid #aaa;display:flex;align-items:center;justify-content:center}
.service .icon.active{background:var(--teal);box-shadow:0 0 0 2px #fff,0 0 0 3px #999}
.service h3{margin-top:10px;font:500 11px/14px 'Roboto',sans-serif;color:var(--teal)}
.service p{margin-top:3px;font-size:8.5px;line-height:11.8px;color:#111}
.service p span{color:var(--teal)}

/* news + testimonials */
.band{top:859px;left:0;width:670px;height:236px;background:var(--light)}
.band-title{font:500 17px 'Roboto',sans-serif;color:var(--ink)}
.band-title b{font-weight:500;color:var(--teal)}
.mini-div{width:58px;height:12px}
.news-item{left:45px;width:270px;height:42px}
.date{left:0;top:0;width:39px;height:40px;border:1px solid #999;border-radius:3px;background:#fff;overflow:hidden;text-align:center}
.date .m{background:var(--teal);color:#fff;font:500 10px/15px 'Roboto',sans-serif}
.date .d{font:500 14px/24px 'Roboto',sans-serif;color:#444}
.news-item h4{left:52px;top:1px;font:700 7.2px 'Lato',sans-serif;color:var(--teal)}
.news-item p{left:52px;top:13px;width:225px;font-size:6.3px;line-height:10px;color:#666}
.quote{left:356px;top:949px;width:269px;height:82px;background:#fff;border:1px solid #c9c9c9;border-radius:5px}
.quote p{position:absolute;left:13px;top:10px;width:240px;text-indent:17px;font:italic 7.2px/12.8px 'Lato',sans-serif;color:#222}
.avatar{left:369px;top:1015px;width:40px;height:40px;border-radius:50%;border:2px solid #fff;box-shadow:0 0 0 1px #bbb;background:radial-gradient(circle at 50% 40%,#e6ddd4,#a9a29a)}
.client{left:414px;top:1041px;font:700 7px 'Lato',sans-serif;color:var(--teal)}

/* footer */
.footnav{top:1095px;left:0;width:670px;height:40px;background:var(--footer-dark)}
.footnav .links{left:46px;top:14px;font:700 8.5px 'Raleway',sans-serif;color:#fff;display:flex;gap:10px}
.social{top:11px;width:18px;height:18px;border-radius:50%;background:#fff}
.footbottom{top:1135px;left:0;width:670px;height:65px;background:var(--teal);color:#fff;font-size:7.5px}
.fi{width:18px;height:18px;border-radius:50%;background:var(--icon-dark);display:flex;align-items:center;justify-content:center}
.footbottom .label{font:700 7.5px 'Lato',sans-serif}
</style>
</head>
<body>

<!-- top bar -->
<div class="abs topbar">
  <div class="abs contact" style="left:48px">
    <svg width="9" height="9" viewBox="0 0 24 24"><path fill="#5ab4c5" d="M6.6 10.8a15 15 0 0 0 6.6 6.6l2.2-2.2a1 1 0 0 1 1-.25 11.4 11.4 0 0 0 3.6.57 1 1 0 0 1 1 1V20a1 1 0 0 1-1 1A17 17 0 0 1 3 4a1 1 0 0 1 1-1h3.5a1 1 0 0 1 1 1c0 1.250.2 2.450.57 3.570a1 1 0 0 1-.25 1z"/></svg>
    <span>+1 555 014 2880</span>
  </div>
  <div class="abs contact" style="left:130px">
    <svg width="11" height="8" viewBox="0 0 22 16"><rect x="1" y="1" width="20" height="14" fill="none" stroke="#5ab4c5" stroke-width="2"/><path d="M1 1l10 8 10-8" fill="none" stroke="#5ab4c5" stroke-width="2"/></svg>
    <span>info@velanest.com</span>
  </div>
  <div class="abs size-tools" aria-label="Text size">
    <span class="btn"><svg width="9" height="9" viewBox="0 0 10 10"><path d="M5 9L1 5h2.5V1h3v4H9z" fill="#fff"/></svg></span>
    <span class="plain">A</span>
    <span class="btn"><svg width="9" height="9" viewBox="0 0 10 10"><path d="M5 1l4 4H6.5v4h-3V5H1z" fill="#fff"/></svg></span>
  </div>
</div>

<!-- header -->
<div class="abs brand"><span class="mark"></span><span class="name">VelaNest</span></div>
<nav class="nav">
  <a class="active" href="#">HOME</a>
  <a href="#" style="left:318px">ABOUT US</a>
  <a href="#" style="left:401px">OUR SERVICES</a>
  <a href="#" style="left:503px">NEWS</a>
  <a href="#" style="left:568px">CONTACT US</a>
</nav>

<!-- hero -->
<section class="abs hero" role="img" aria-label="Photo of a smiling young carer hugging an elderly woman, with medical staff blurred in the background">
  <div class="abs arrow" style="left:4px;top:127px"><svg width="7" height="9" viewBox="0 0 7 9"><path d="M6 1L2 4.5 6 8" stroke="#fff" stroke-width="2" fill="none"/></svg></div>
  <div class="abs arrow" style="left:645px;top:127px"><svg width="7" height="9" viewBox="0 0 7 9"><path d="M1 1l4 3.5L1 8" stroke="#fff" stroke-width="2" fill="none"/></svg></div>
  <div class="abs caption">We specialize in helping and supporting elderly people</div>
</section>

<!-- welcome -->
<section class="abs welcome">
  <h1 class="abs title" style="top:30px">WELCOME TO <b>VelaNest</b></h1>
  <svg class="abs divider" style="top:57px" viewBox="0 0 100 12"><line x1="0" y1="6" x2="40" y2="6" stroke="#ccc"/><line x1="60" y1="6" x2="100" y2="6" stroke="#ccc"/><circle cx="50" cy="6" r="6" fill="#5ab4c5"/></svg>
  <p class="abs">Sed ut perspiciatis unde omnis iste natus error sit voluptatem accusantium dolo remque laudantium, totam rem aperiam, eaque ipsa quae ab illo inventore veritatis et quasi architecto beatae vitae dicta sunt explicabo. Sed ut perspiciatis unde omnis iste natus error sit voluptatem accusantium dolo. Sed ut perspiciatis unde omnis iste natus error sit voluptatem accusantium dolo.Sed ut perspiciatis unde omnis iste natus error sit voluptatem accusantium dolor quasi architecto beatae vitae dicta sunt explicabo.</p>
  <a class="abs cta" href="#">READ MORE<i><svg width="14" height="14" viewBox="0 0 14 14"><path d="M6 4l3 3-3 3" stroke="#5ab4c5" stroke-width="1.6" fill="none"/></svg></i></a>
</section>

<!-- services -->
<h2 class="abs title" style="top:617px">OUR <b>SERVICES</b></h2>
<svg class="abs divider" style="top:648px" viewBox="0 0 100 12"><line x1="0" y1="6" x2="40" y2="6" stroke="#ccc"/><line x1="60" y1="6" x2="100" y2="6" stroke="#ccc"/><circle cx="50" cy="6" r="6" fill="#5ab4c5"/></svg>

<div class="abs service" style="left:43px">
  <div class="icon active"><svg width="30" height="28" viewBox="0 0 30 28"><path d="M9 2c-2 2 2 3 0 6M14 2c-2 2 2 3 0 6" stroke="#fff" stroke-width="1.5" fill="none"/><path d="M5 11h17v5a8 8 0 0 1-8 8h-1a8 8 0 0 1-8-8z" fill="#fff"/><path d="M22 13h2a3 3 0 0 1 0 6h-2" stroke="#fff" stroke-width="2" fill="none"/><rect x="2" y="25" width="24" height="2" rx="1" fill="#fff"/></svg></div>
  <h3>Going Out For A Cup<br>Of Coffee</h3>
  <p>Lorem ipsum dolor sit amet, consectetuer adipiscing elit, sed diam nonummy nibh euis...<span>[+]</span></p>
</div>
<div class="abs service" style="left:194px">
  <div class="icon"><svg width="24" height="34" viewBox="0 0 24 34"><circle cx="13" cy="4" r="3.5" fill="#5ab4c5"/><path d="M12 9l-5 5 1 7M12 9l2 9 5 4M12 9l6 6 4-1M14 18l-4 7-4 7M14 18l2 6 3 8" stroke="#5ab4c5" stroke-width="3" stroke-linecap="round" fill="none"/></svg></div>
  <h3>Walk In The<br>Park</h3>
  <p>Lorem ipsum dolor sit amet, consectetuer adipiscing elit, sed diam nonummy nibh euis...<span>[+]</span></p>
</div>
<div class="abs service" style="left:346px">
  <div class="icon"><svg width="34" height="28" viewBox="0 0 34 28"><path d="M2 12L17 2l15 10v14H2z" fill="none" stroke="#5ab4c5" stroke-width="2.5"/><circle cx="12" cy="14" r="3" fill="#5ab4c5"/><circle cx="22" cy="14" r="3" fill="#5ab4c5"/><path d="M6 23a6 5 0 0 1 12 0zM16 23a6 5 0 0 1 12 0z" fill="#5ab4c5"/></svg></div>
  <h3>Help In<br>Household</h3>
  <p>Lorem ipsum dolor sit amet, consectetuer adipiscing elit, sed diam nonummy nibh euis...<span>[+]</span></p>
</div>
<div class="abs service" style="left:498px">
  <div class="icon"><svg width="36" height="30" viewBox="0 0 36 30"><rect x="15" y="2" width="19" height="12" rx="2" fill="none" stroke="#5ab4c5" stroke-width="1.6"/><path d="M19 14l-2 4 5-4" fill="#5ab4c5"/><line x1="19" y1="7" x2="30" y2="7" stroke="#5ab4c5" stroke-width="1.4"/><line x1="19" y1="10" x2="27" y2="10" stroke="#5ab4c5" stroke-width="1.4"/><circle cx="10" cy="16" r="5" fill="#5ab4c5"/><path d="M1 30a9 8 0 0 1 18 0z" fill="#5ab4c5"/></svg></div>
  <h3>Having<br>Conversations</h3>
  <p>Lorem ipsum dolor sit amet, consectetuer adipiscing elit, sed diam nonummy nibh euis...<span>[+]</span></p>
</div>

<!-- news + testimonials -->
<section class="abs band"></section>
<h2 class="abs band-title" style="left:46px;top:890px"><b>LATEST</b> NEWS</h2>
<svg class="abs" style="left:294px;top:895px" width="20" height="10" viewBox="0 0 20 10"><path d="M6 1L2 5l4 4M14 1l4 4-4 4" stroke="#444" stroke-width="1.6" fill="none"/></svg>
<svg class="abs mini-div" style="left:45px;top:919px" viewBox="0 0 58 12"><circle cx="8" cy="6" r="6" fill="#5ab4c5"/><line x1="18" y1="6" x2="58" y2="6" stroke="#ccc"/></svg>
<div class="abs" style="left:335px;top:905px;width:1px;height:170px;background:#ddd"></div>

<div class="abs news-item" style="top:956px">
  <div class="abs date"><div class="m">MAY</div><div class="d">12</div></div>
  <h4 class="abs">Lorem ipsum dolor sit amet Lorem ipsum dolor sit.</h4>
  <p class="abs">Lorem ipsum dol adipiscing elit, seder Dollar smit quis nostrud exerci tation adipiscing elit adipiscing elit, seder Dollar smit quis nostrud</p>
</div>
<div class="abs news-item" style="top:1013px">
  <div class="abs date"><div class="m">MAY</div><div class="d">12</div></div>
  <h4 class="abs">Lorem ipsum dolor sit amet Lorem ipsum dolor sit.</h4>
  <p class="abs">Lorem ipsum dol adipiscing elit, seder Dollar smit quis nostrud exerci tation adipiscing elit adipiscing elit, seder Dollar smit quis nostrud</p>
</div>

<h2 class="abs band-title" style="left:355px;top:890px"><b>CLIENT</b> TESTIMONIALS</h2>
<svg class="abs" style="left:606px;top:895px" width="20" height="10" viewBox="0 0 20 10"><path d="M6 1L2 5l4 4M14 1l4 4-4 4" stroke="#444" stroke-width="1.6" fill="none"/></svg>
<svg class="abs mini-div" style="left:355px;top:919px" viewBox="0 0 58 12"><circle cx="8" cy="6" r="6" fill="#5ab4c5"/><line x1="18" y1="6" x2="58" y2="6" stroke="#ccc"/></svg>

<div class="abs quote">
  <svg class="abs" style="left:12px;top:9px" width="13" height="10" viewBox="0 0 14 11"><path d="M0 11V6L3 0h3L4 5h2v6zM8 11V6l3-6h3l-2 5h2v6z" fill="#bbb"/></svg>
  <p>Lorem ipsum dolor sit amet consetug e sed diay nibh euismodl tincidunt ut laoreet dolore magam er vol wisi enim ad minim veniam quis nostrud exerci tationorem ipsum dolor sit ametee sed diammmy nibh euismd tincidunt ut laoreet dolore magna aliqur volpatl tiidunt ut</p>
</div>
<svg class="abs" style="left:553px;top:1030px" width="34" height="15" viewBox="0 0 34 15"><path d="M0 0.5L2 14 34 0.5" fill="#fff" stroke="#c9c9c9"/><rect x="0" y="-1" width="34" height="1.5" fill="#fff"/></svg>
<div class="abs avatar" role="img" aria-label="Portrait photo of the client"></div>
<div class="abs client">Mrs. Ada Brennel</div>

<!-- footer -->
<footer>
  <div class="abs footnav">
    <div class="abs links"><span>Home</span><span>I</span><span>About Us</span><span>I</span><span>Our Services</span><span>I</span><span>News</span><span>I</span><span>Contact Us</span></div>
    <span class="abs social" style="left:581px" aria-label="Social profile link"></span>
    <span class="abs social" style="left:606px" aria-label="Social feed link"></span>
  </div>
  <div class="abs footbottom">
    <div class="abs fi" style="left:46px;top:23px"><svg width="8" height="10" viewBox="0 0 8 10"><path d="M4 0a4 4 0 0 1 4 4c0 3-4 6-4 6S0 7 0 4a4 4 0 0 1 4-4z" fill="#fff"/><circle cx="4" cy="4" r="1.5" fill="#4b4b4b"/></svg></div>
    <div class="abs" style="left:70px;top:21px;line-height:13px"><div class="label">VELANEST</div>48, Linden Row, Harbourside - 204518</div>
    <div class="abs fi" style="left:230px;top:23px"><svg width="8" height="8" viewBox="0 0 24 24"><path fill="#fff" d="M6.6 10.8a15 15 0 0 0 6.6 6.6l2.2-2.2a1 1 0 0 1 1-.25 11.4 11.4 0 0 0 3.6.57 1 1 0 0 1 1 1V20a1 1 0 0 1-1 1A17 17 0 0 1 3 4a1 1 0 0 1 1-1h3.5a1 1 0 0 1 1 1c0 1.25.2 2.45.57 3.57a1 1 0 0 1-.25 1z"/></svg></div>
    <div class="abs" style="left:253px;top:21px;line-height:13px"><div class="label">Call Us :</div>+1 555 014 2880</div>
    <div class="abs fi" style="left:329px;top:23px"><svg width="9" height="7" viewBox="0 0 22 16"><rect x="1" y="1" width="20" height="14" fill="#fff"/><path d="M1 1l10 8 10-8" fill="none" stroke="#4b4b4b" stroke-width="2"/></svg></div>
    <div class="abs" style="left:353px;top:21px;line-height:13px"><div class="label">Email Us :</div>info@velanest.com</div>
    <div class="abs" style="left:566px;top:10px;width:26px;height:26px;border-radius:50%;background:var(--icon-dark)"></div>
    <div class="abs" style="left:500px;top:42px;width:124px;text-align:right;font-size:7px;line-height:9px">Copyright © 2016 VelaNest.<br>All Rights Reserved.</div>
  </div>
</footer>

</body>
</html>
```